Broschüre für eine Trainingsakademie
Zielgruppe
Ich möchte eine Broschüre zu meinem Unternehmen und meinen Angeboten schöner Design haben.
Ich bin Trainer/ Coach für moderne Personalstrategien insbesondere für die Personalgewinnung, Mitarbeiterbindung und -entwicklung. Zudem biete ich Trainings und Coachings für Mitarbeiter und Führungskräfte an. Zum Beispiel zu Themen wie gesunde Führung, Stressmanagement, Resilienz usw.
Meine Zielgruppe sind vor allem mittelständische Unternehmen oder junge aufstrebende StartUps, die ich beim Aufbau von Personalstrukturen unterstütze.
Aufgabenstellung
Mein Logo und die Farben sollen entsprechend berücksichtigt werden. Ein Entwurf für die Broschüre besteht bereits. Das ist allerdings nur meine Idee, als Laie. Ich hätte hier gern professionelle Ideen, so dass die Broschüre professionell und ansprechend wirkt.
Bilder habe ich eigentlich - diese finden sich auch auf meiner Homepage. Allerdings bin ich gerade auch beim Deckblatt offen. Auch für andere Gestaltungsvorschläge.

```html
<!DOCTYPE html>
<html lang="de">
<head>
<meta charset="utf-8">
<title>Lindqvist Coaching – Trainingsakademie Broschüre</title>
<link rel="stylesheet" href="https://fonts.googleapis.com/css2?family=Arimo:wght@400;700&family=Roboto+Condensed:wght@400;700&family=Noto+Serif:ital@1&display=swap">
<style>
:root{
  --bg:#f4f4f5;
  --paper:#ececee;
  --paper-light:#f2f2f3;
  --purple:#6f6782;
  --purple-dark:#5c5472;
  --lilac:#c9c5d3;
  --lilac-soft:#d9d6e0;
  --ink:#4a4458;
  --ink-soft:#6b6578;
  --white:#ffffff;
  --accent:#e0465d;
}
*{box-sizing:border-box;margin:0;padding:0}
html,body{width:1200px;height:2168px;overflow:hidden;background:var(--bg)}
body{font-family:"Arimo",Arial,sans-serif;color:var(--ink);display:flex;flex-direction:column;align-items:center;justify-content:center;gap:260px}
.spread{display:flex;width:1120px;height:620px;box-shadow:0 18px 40px rgba(60,50,80,.18)}
.panel{width:280px;height:620px;padding:24px 22px;overflow:hidden;position:relative;background:var(--paper)}
.panel + .panel{border-left:1px solid rgba(0,0,0,.06)}
.panel--purple{background:var(--purple);color:var(--white)}
.panel--light{background:var(--paper-light)}
.title{font-weight:700;font-size:15px;line-height:1.15;color:var(--ink-soft)}
.panel--purple .title{color:var(--white)}
.rule{width:78px;height:1.5px;background:rgba(255,255,255,.8);margin:16px 0}
.lead{font-size:10px;line-height:1.3;font-weight:700;margin-bottom:14px}
.sub{font-size:9.5px;line-height:1.3;margin:4px 0 4px}
.body{font-family:"Roboto Condensed",sans-serif;font-size:7.6px;line-height:1.38}
.icon{width:22px;height:22px;margin-top:10px;opacity:.7}
.num{font-size:10px;color:var(--ink-soft);margin-top:12px}
.arrow-step{position:relative}
.arrow-step::before{content:"";position:absolute;left:-22px;top:-8px;border-left:9px solid var(--lilac);border-top:9px solid transparent;border-bottom:9px solid transparent}
.numhead{font-size:9.5px;line-height:1.3;color:var(--ink-soft);margin:3px 0 3px}
.photo{height:92px;margin:-24px -22px 16px;background:linear-gradient(180deg,#a9c2d8 0%,#c9d4da 38%,#8a8a57 55%,#6f6a4c 80%,#8a6a6e 100%)}
.para{font-size:9px;line-height:1.32;margin-bottom:12px}
.para.dim{color:#d9d5e2}
.contact{display:flex;gap:14px;margin-top:22px;font-family:"Roboto Condensed",sans-serif;font-size:7px;line-height:1.5;color:#e5e2ec}
.logo-box{background:var(--purple-dark);margin:-24px 0 0 -4px;width:178px;height:70px;display:flex;align-items:center;justify-content:center}
.logo-name{font-family:"Arimo",sans-serif;font-weight:400;font-size:13px;letter-spacing:1.5px;color:var(--white);text-transform:uppercase}
.cover-title{font-weight:700;font-size:19px;color:var(--ink);margin-top:78px}
.cover-sub{font-weight:700;font-size:14px;line-height:1.3;color:#8e889c;margin-top:12px}
.illus{position:absolute;border-radius:50% 46% 40% 50%}
.badge{position:absolute;left:38px;top:400px;width:56px;height:56px;border-radius:50%;background:var(--accent);color:var(--white);font-size:5.5px;line-height:1.3;text-align:center;display:flex;align-items:center;justify-content:center}
.url{position:absolute;left:22px;bottom:28px;font-family:"Roboto Condensed",sans-serif;font-size:7px;color:var(--ink)}
.quote-box{background:var(--purple);color:var(--white);margin:10px -22px 0;padding:18px 22px 12px 22px}
.quote{font-family:"Noto Serif",serif;font-style:italic;font-size:7.6px;line-height:1.32;color:#e6e3ec;margin-bottom:9px}
.signname{font-size:7px;letter-spacing:.5px;color:#d3cfe0;margin-top:6px}
.portrait{position:absolute;right:16px;top:316px;width:74px;height:84px;background:linear-gradient(180deg,#cfc9c6,#b8aca4 60%,#8e8590)}
.letter{font-family:"Roboto Condensed",sans-serif;font-size:7px;line-height:1.4;width:132px;margin-top:16px}
.caption{position:absolute;right:14px;top:408px;width:80px;font-family:"Roboto Condensed",sans-serif;font-size:4.6px;line-height:1.45;color:var(--ink-soft)}
.pillars{font-size:8px;line-height:1.35;margin:8px 0}
.signature{width:70px;height:20px;margin-top:8px}
.magnet-head{font-weight:700;font-size:13px;line-height:1.2;color:var(--ink-soft);margin:22px 0 0 86px}
.hand{position:absolute;left:14px;top:24px;width:80px;height:60px;background:linear-gradient(135deg,#e4e2e8,#d6d3dc);border-radius:40% 30% 50% 40%}
.text{font-size:8.2px;line-height:1.32;color:var(--ink-soft);margin-bottom:9px}
.benefit{display:flex;gap:10px;margin-top:14px}
.benefit svg{flex:none;width:22px;height:22px}
.benefit h5{font-size:8px;font-weight:400;color:var(--ink-soft);margin-bottom:3px}
.benefit ul{list-style:none;font-family:"Roboto Condensed",sans-serif;font-size:6.4px;line-height:1.45}
.benefit li::before{content:"■ ";font-size:5px;color:var(--purple)}
.offer-title{font-weight:700;font-size:11px;color:var(--ink);margin-bottom:12px}
.offer-box{background:var(--lilac);margin:0 -2px 14px;padding:0 0 10px}
.offer-box h4{background:var(--lilac-soft);font-size:10px;font-weight:400;padding:14px 10px 10px;margin-bottom:8px}
.item{padding:0 10px;margin-top:7px}
.item h5{font-size:8px;font-weight:400;margin-bottom:2px}
.item p{font-family:"Roboto Condensed",sans-serif;font-size:6.3px;line-height:1.4}
.ladder{position:absolute;left:22px;top:36px;width:70px;height:160px;background:linear-gradient(180deg,#8b84a8,#5d57a0 60%,#b7b3c8);border-radius:8px}
.logo-plain{position:absolute;right:26px;top:50px;font-family:"Arimo",sans-serif;font-size:11px;letter-spacing:1.5px;color:var(--ink);text-transform:uppercase}
.compass{position:absolute;right:24px;bottom:60px;width:90px;height:90px;border-radius:50%;background:radial-gradient(circle,#e8e7eb,#dddbe2)}
.develop{position:absolute;left:22px;right:22px;top:240px}
</style>
</head>
<body>

<!-- Aussenseite -->
<section class="spread" aria-label="Außenseite der Broschüre">
  <article class="panel panel--purple">
    <h2 class="title">Trainings und Coachings<br>mit Mehrwert</h2>
    <div class="rule"></div>
    <p class="lead">Damit die Trainings und Coachings wirklich in der Praxis umgesetzt werden und einen langfristigen Mehrwert bieten:</p>
    <svg class="icon" viewBox="0 0 24 24" fill="none" stroke="#fff" stroke-width="1.2"><circle cx="12" cy="12" r="10"/><circle cx="12" cy="12" r="6"/><circle cx="12" cy="12" r="2"/></svg>
    <h4 class="sub">Training aus der Praxis für die Praxis:</h4>
    <p class="body">Über 12 Jahre relevante Berufserfahrung im Personalwesen/ in der Personalleitung in internationalen renommierten Unternehmen, Führungserfahrung und die Leitung eines Profit Centers im Handel bilden das Rüstzeug für Lindqvist Coaching. Ihre Probleme des Alltags kenne ich nicht nur aus der Theorie, sondern aus dem eigenen Berufsleben!</p>
    <svg class="icon" viewBox="0 0 24 24" fill="none" stroke="#fff" stroke-width="1.2"><circle cx="5" cy="6" r="2.5"/><circle cx="19" cy="6" r="2.5"/><circle cx="12" cy="18" r="2.5"/><path d="M7 7l4 9M17 7l-4 9M7.5 6h9"/></svg>
    <h4 class="sub">Methoden mit System:</h4>
    <p class="body">In den Trainings und Coachings wird mit wissenschaftlich erprobten Methoden, Tests und Konzepten gearbeitet. Die Eignungsdiagnostik orientiert sich an den Anforderungen der DIN 33430 und wendet Tests an, die diesen Kriterien entsprechen. Coaching Ausbildungen in den Bereichen Business Coaching, Hypnose Coaching, NLP, Stress- und Mentalcoaching bieten eine große Varianz an Trainingsmethoden, die je nach Anforderung situationsgerecht und effektiv angewendet werden.</p>
    <svg class="icon" viewBox="0 0 24 24" fill="none" stroke="#fff" stroke-width="1.2"><circle cx="7" cy="8" r="3"/><circle cx="17" cy="8" r="3"/><path d="M2 20c0-4 2-6 5-6s5 2 5 6M12 20c0-4 2-6 5-6s5 2 5 6"/></svg>
    <h4 class="sub">Begleitung in die Praxis:</h4>
    <p class="body">Viele gute Seminare verlieren ihre Wirkung, weil die gewonnenen Erkenntnisse und Inhalte im persönlichen Berufsalltag nicht umgesetzt werden können. Meine Personal-Erfolgs-Strategie beinhaltet deshalb immer ein passgenaues Coaching/ Training sowie eine gezielte Umsetzungsbegleitung. Diese schließt neben den Seminar-Teilnehmern auch die Vorgesetzten und/oder Personalabteilung ein.</p>
  </article>

  <article class="panel panel--light">
    <h2 class="title">Was können Sie als Arbeitgeber<br>nun konkret dafür tun?</h2>
    <div class="arrow-step"><p class="num">1.</p>
    <h4 class="numhead">Wenn das Unternehmen zum Mitarbeiter passt – und umgekehrt – dann klappt es auch mit dem Wohlfühl-Klima.</h4>
    <p class="body">Employer Branding ist daher für alle Arbeitgeber hochrelevant: Was macht uns aus und was bieten wir unseren Angestellten? Welche Mitarbeiter passen zu uns? Eine ehrliche Bestandsaufnahme und Kommunikation bildet dafür die Basis.</p></div>
    <div class="arrow-step"><p class="num">2.</p>
    <h4 class="numhead">Anerkennung für gute Arbeit.</h4>
    <p class="body">Das muss nicht unbedingt mit finanziellem Aufwand verbunden sein. Ein ehrliches Lob motiviert Mitarbeiter ungleich stärker als z.&nbsp;B. unpersönliche Motivations-Poster in der Kantine.</p></div>
    <div class="arrow-step"><p class="num">3.</p>
    <h4 class="numhead">Feedback-Kultur schaffen und pflegen.</h4>
    <p class="body">Monatlich oder quartalsweise stattfindende Vier-Augen-Gespräche, wöchentliche Team-Kickoffs oder das 5-Minutengespräch zwischendurch helfen.</p></div>
    <div class="arrow-step"><p class="num">4.</p>
    <h4 class="numhead">Als Arbeitgeber ansprechbar und nahbar bleiben.</h4>
    <p class="body">Das ist etwas, was täglich gezeigt werden kann. Hier haben kleinere Unternehmen große Chancen!</p></div>
    <div class="arrow-step"><p class="num">5.</p>
    <h4 class="numhead">Weiterbildungsmöglichkeiten bieten.</h4>
    <p class="body">Zeigen Sie, dass Ihnen die Entwicklung Ihrer Mitarbeiter wichtig ist. Davon profitiert auch das Unternehmen.</p></div>
    <div class="arrow-step"><p class="num">6.</p>
    <h4 class="numhead">Entwicklungsperspektiven bieten!</h4>
    <p class="body">Viele Mitarbeiter können sich nur durch eine Führungskarriere weiterentwickeln. Fachkarrieren können hier eine attraktive Alternative bieten.</p></div>
  </article>

  <article class="panel panel--purple">
    <div class="photo" role="img" aria-label="Landschaftsfoto der blühenden Heide unter blauem Himmel"></div>
    <h2 class="title" style="font-size:13.5px">Lindqvist Coaching –<br>Die Trainingsakademie aus der schönen Lüneburger Heide</h2>
    <div class="rule"></div>
    <p class="para">Mitten in der schönen Lüneburger Heide zwischen Hamburg, Hannover und Bremen ist der Sitz von Lindqvist Coaching. Hier wird immer am Zahn der Zeit neues Wissen, neue Forschungsergebnisse und Trends aus dem Personalmanagement gebündelt und für die Kunden aufbereitet, damit Sie immer die beste Beratung erhalten!</p>
    <p class="para dim">Digital oder in Präsenz – in einzelnen Modulen oder als Tagestrainings – Inhouse oder Seminarhotel:</p>
    <p class="para">Die Coachings und Trainings werden entsprechend den Anforderungen und Bedürfnissen der Auftraggeber konzipiert! Der persönliche Kontakt und Austausch wird in Präsenztrainings besonders geschätzt.</p>
    <p class="para">Nutzen Sie die Vorteile virtueller Trainings und Coaching für das modulare Training und individuelle Coaching sowie die Umsetzungsbegleitung.</p>
    <p class="para dim">Informieren Sie sich jetzt und erhalten Sie ein maßgeschneidertes Angebot!</p>
    <div class="contact">
      <address style="font-style:normal">Lindqvist Coaching<br>Marlene Lindqvist<br>Am Birkenweg 8<br>29600 Heidebrück</address>
      <p>05100 / 12 345 67<br>0170 / 00 111 22<br>kontakt@lindqvist-coaching.com<br>www.marlene-lindqvist.de</p>
    </div>
  </article>

  <article class="panel panel--light">
    <div class="logo-box"><span class="logo-name">Lindqvist Coaching</span></div>
    <h1 class="cover-title">Trainingsakademie</h1>
    <p class="cover-sub">für Personalstrategie,<br>Personalentwicklung und<br>Personalführung</p>
    <div class="illus" role="img" aria-label="Illustration einer Frau am Schreibtisch mit Laptop, Lampe und Pflanze" style="left:60px;top:390px;width:190px;height:170px;background:radial-gradient(circle at 55% 50%,#7d77c9 0%,#d8d6e4 45%,#e6e5eb 75%,transparent 76%)"></div>
    <div class="badge">DIGITAL<br>ODER<br>IN PRÄSENZ</div>
    <p class="url">www.marlene-lindqvist.de</p>
  </article>
</section>

<!-- Innenseite -->
<section class="spread" aria-label="Innenseite der Broschüre">
  <article class="panel panel--light">
    <h2 class="title" style="font-size:12.5px">Entwickeln Sie für Ihr Unternehmen eine individuelle und auf die eigenen Bedürfnisse zugeschnittene Personal-Erfolgs-Strategie:</h2>
    <div class="quote-box">
      <p class="quote">Ein Unternehmen sollte sich daran orientieren, ob es genug gute Leute anziehen kann, um seinen Wachstum und seinen Erfolg langfristig zu gestalten.</p>
      <p class="quote">Die richtigen Talente einzustellen braucht die richtige Strategie, die richtigen Fragen und eine gesunde Portion Neugierde.</p>
      <p class="quote">Denn kein Lebenslauf kann Ihnen sagen, ob jemand zu Ihrer Firmenkultur passt. Einstellen war, ist und bleibt der wichtigste Job, den Sie für Ihren Unternehmenserfolg haben.</p>
      <p class="quote">Hat ein Unternehmen die richtigen Mitarbeiter gefunden, sollte es alles daransetzen, diese Mitarbeiter langfristig zufrieden im Unternehmen zu halten.</p>
      <p class="signname">MARLENE LINDQVIST</p>
    </div>
    <div class="portrait" role="img" aria-label="Porträtfoto der Trainerin"></div>
    <p class="caption">Als langjährige Spezialistin und Führungskraft im Personalwesen kenne ich die Anforderungen an Mitarbeiter und Führungskräfte sehr genau. Mein Coachingansatz verbindet Fach- und Ausbildungswissen mit Mental-, Stress- und Hypnose-Coaching.</p>
    <div class="letter">
      <p>Damit dies gelingt, unterstützt Lindqvist Coaching Unternehmen bei der Entwicklung und dem Aufbau einer individuellen, genau auf die Unternehmensbedürfnisse angepassten Personal-Erfolgs-Strategie. Diese baut auf drei Säulen auf:</p>
      <p class="pillars">1. Personalstrategie<br>2. Personalentwicklung<br>3. Personalführung</p>
      <p>Lassen Sie sich jetzt beraten und erfahren Sie, wie Lindqvist Coaching Sie bei Ihren Zielen unterstützen kann.</p>
      <p style="margin-top:8px">Herzlichst</p>
      <svg class="signature" viewBox="0 0 70 20" fill="none" stroke="#8e88b8" stroke-width="1"><path d="M2 14c8-10 12 6 20-2s10 4 18-2 10 2 28-4"/></svg>
    </div>
  </article>

  <article class="panel panel--light">
    <div class="hand" role="img" aria-label="Linienzeichnung einer Hand mit Magnet"></div>
    <h2 class="magnet-head">Werden Sie zum Magneten für Ihre Mitarbeiter und Bewerber!</h2>
    <div style="margin-top:30px">
      <p class="text">Der Kampf um die besten Köpfe hat längst begonnen. Gute Bewerber können sich Ihre Arbeitgeber oft aussuchen. Viele Arbeitnehmer erhalten regelmäßig Anfragen von Headhuntern und Personaldienstleistern, die Ihre Mitarbeiter abwerben wollen. Was können Sie tun?</p>
      <p class="text">Zahlreiche Studien der letzten Jahre zeigen uns, was Mitarbeitern bei Ihren Arbeitgebern hält und was ihnen in ihrem Job wichtig ist. Fangen Sie heute an, Ihre Mitarbeiter an Ihr Unternehmen zu binden!</p>
      <p class="text">Was sich Arbeitnehmer von Ihren Arbeitgebern wünschen:</p>
    </div>
    <div class="benefit">
      <svg viewBox="0 0 24 24" fill="none" stroke="#6f6782" stroke-width="1.2"><circle cx="12" cy="12" r="9"/><path d="M8 14c2 2.5 6 2.5 8 0"/><circle cx="9" cy="10" r=".8"/><circle cx="15" cy="10" r=".8"/></svg>
      <div><h5>Wohlgefühl bei der Arbeit</h5>
      <ul><li>Wertschätzung der Arbeit</li><li>Regelmäßiges Feedback/ eine gute Feedbackkultur</li><li>Unterstützung bei Fragen und Problemen</li><li>Gute Beziehung zu den Vorgesetzten und Kollegen</li><li>Faire und attraktive Bezahlung</li></ul></div>
    </div>
    <div class="benefit" style="margin-left:24px">
      <svg viewBox="0 0 24 24" fill="none" stroke="#6f6782" stroke-width="1.2"><path d="M12 3v18M4 7h16M4 7l-2 7h4zM20 7l-2 7h4zM8 21h8"/></svg>
      <div><h5>Eine gesunde Work-Life-Balance</h5>
      <ul><li>Flexible Arbeitszeiten/ Arbeitszeitmodelle</li><li>Karriere in Teilzeit</li><li>Stressreduktion</li></ul></div>
    </div>
    <div class="benefit">
      <svg viewBox="0 0 24 24" fill="none" stroke="#6f6782" stroke-width="1.2"><path d="M12 3l2.6 5.3 5.9.9-4.3 4.1 1 5.8L12 16.4 6.8 19.1l1-5.8L3.5 9.2l5.9-.9z"/></svg>
      <div><h5>Entwicklungsmöglichkeiten und Weiterbildungsangebote für Mitarbeiter</h5>
      <ul><li>Regelmäßige Weiterbildungsangebote zur fachlichen und persönlichen Weiterentwicklung</li><li>Anerkennung für geleistete Arbeit</li><li>Attraktive Karrierepfade</li></ul></div>
    </div>
  </article>

  <article class="panel panel--light">
    <h3 class="offer-title">Das Trainingsangebot:</h3>
    <section class="offer-box">
      <h4>Personalstrategie</h4>
      <div class="item"><h5>Strategische Personalauswahl:</h5><p>Von der richtigen Anforderungsanalyse über die Ausschreibung zum Bewerbungs- und Auswahlprozess bis zum gelungenen Onboarding – ausgerichtet auf Ihr Employer Branding.</p></div>
      <div class="item"><h5>Eignungsdiagnostik:</h5><p>Von der Auswahl einzelner Tests bis zur Konzeption und Begleitung von Bewerbertagen ausgerichtet auf die jeweilige Stellenanforderung.</p></div>
      <div class="item"><h5>Strategische Mitarbeiterplanung und -bindung:</h5><p>Entwicklung von Strukturen zur Mitarbeiterbindung und -entwicklung auch im Hinblick auf Personalkennzahlen.</p></div>
    </section>
    <section class="offer-box">
      <h4>Personalführung</h4>
      <div class="item"><h5>Führungskräfte Coaching – Mental fit Führen:</h5><p>(Digitale-) Führung, Stressmanagement, Konfliktmanagement, Motivationsthemen, Mentale Stärke, Resilienz, Ressourcenaufbau und Zeitmanagement sind nur einige Inhalte, die in diesem Coachingprogramm neben individuellen Themen bearbeitet werden.</p></div>
      <div class="item"><h5>Mitarbeiter Coaching – Auf dem Weg zur Führungskraft:</h5><p>Vorbereitung und Begleitung Ihres Mitarbeiters auf dem Weg zur Führungskraft.</p></div>
      <div class="item"><h5>Gruppentrainings zu gesunder Führung:</h5><p>Mitarbeiter motivierend Führen, Vorbild sein, Stressmanagement, Konflikte meistern und effektive Führung sind hier einige Themen, die in diesem Training betrachtet werden.</p></div>
    </section>
  </article>

  <article class="panel panel--light">
    <div class="ladder" role="img" aria-label="Illustration eines Mannes auf einer Leiter mit Blick in die Ferne"></div>
    <span class="logo-plain">Lindqvist Coaching</span>
    <section class="offer-box develop">
      <h4>Personalentwicklung</h4>
      <div class="item"><h5>Mitarbeiter Coaching – Mental fit im Arbeitsleben:</h5><p>Stressmanagement, Konfliktmanagement, Motivationsthemen, Mentale Stärke, Resilienz und Ressourcenaufbau sind nur einige Inhalte, die in diesem Coachingprogramm neben individuellen Themen bearbeitet werden.</p></div>
      <div class="item"><h5>Mitarbeiter-Trainings/ Gruppentrainings:</h5><p>Ich biete Seminare zu Resilienz und Stressmanagement, effizientes und effektives Management/ Zeitmanagement, Ressourcenaufbau und mentale Stärke, Stressmanagement oder Konfliktmanagement an.</p></div>
      <div class="item"><h5>Mitarbeiterbegleitung – Outplacement:</h5><p>Ich unterstütze Ihre Mitarbeiter im Trennungsprozess bei der Bestandsaufnahme, Kompetenzanalyse, Karriereplanung sowie dem Bewerbungscoaching und begleite die Umsetzung bis zum neuen Job.</p></div>
    </section>
    <div class="compass" role="img" aria-label="Dezente Linienzeichnung eines Kompasses"></div>
    <p class="url">www.marlene-lindqvist.de</p>
  </article>
</section>

</body>
</html>
```